Kettlebrook Fixers Co. Business Card & Stationary
Roving Gadget Mend Service
Bright & Fun-filled
Dorian P. Hale
Service Director
P.O. Box 530697
Larkhaven, TX 77390
dphale@corvanmail.com
Expert Repair on All Major Brands & Models.
Mention this Special for $15 Off Any Job Requiring Parts!

```html
<!DOCTYPE html>
<html lang="en">
<head>
<meta charset="utf-8">
<title>Kettlebrook Fixers Co. Business Card</title>
<link rel="stylesheet" href="https://fonts.googleapis.com/css2?family=Arimo:ital,wght@0,400;0,700;1,400&display=swap">
<style>
  :root {
    --backdrop: #e6e7e8;
    --card: #ffffff;
    --brand-blue: #29a9e0;
    --brand-navy: #12466f;
    --accent-yellow: #f5d000;
    --text-grey: #6d6e71;
    --rule-grey: #dcdddf;
  }
  html, body {
    margin: 0;
    width: 1200px;
    height: 838px;
    overflow: hidden;
    background: var(--backdrop);
    font-family: "Arimo", Arial, sans-serif;
  }
  .business-card {
    position: absolute;
    left: 100px;
    top: 133px;
    width: 1000px;
    height: 572px;
    background: var(--card);
    box-shadow: 0 6px 22px rgba(0,0,0,0.12);
    overflow: hidden;
  }
  .brand-mark {
    position: absolute;
    left: 60px;
    top: 150px;
    width: 380px;
    height: 200px;
    display: flex;
    align-items: center;
    gap: 18px;
  }
  .brand-dot {
    flex: none;
    width: 34px;
    height: 34px;
    border-radius: 50%;
    background: var(--brand-blue);
  }
  .brand-name {
    font-weight: 700;
    font-size: 38px;
    line-height: 1.1;
    color: var(--brand-navy);
  }
  .divider {
    position: absolute;
    left: 490px;
    top: 70px;
    width: 1px;
    height: 390px;
    background: var(--rule-grey);
  }
  .contact-block {
    position: absolute;
    left: 530px;
    top: 150px;
    color: var(--text-grey);
  }
  .contact-name {
    margin: 0;
    font-size: 40px;
    font-weight: 700;
    letter-spacing: 2px;
    color: var(--brand-blue);
  }
  .contact-title {
    margin: 4px 0 26px;
    font-size: 19px;
  }
  .contact-address, .contact-lines {
    margin: 0;
    font-size: 19px;
    line-height: 1.35;
  }
  .contact-lines { margin-top: 18px; }
  .contact-label {
    display: inline-block;
    width: 26px;
    font-weight: 700;
    color: var(--accent-yellow);
  }
  .promo-band {
    position: absolute;
    left: 0;
    bottom: 0;
    width: 100%;
    height: 46px;
    background: var(--brand-blue);
    border-bottom: 6px solid var(--accent-yellow);
    display: flex;
    align-items: center;
    padding-left: 40px;
    box-sizing: border-box;
    color: var(--card);
    font-style: italic;
    font-size: 17px;
    gap: 16px;
  }
</style>
</head>
<body>
  <div class="business-card">
    <div class="brand-mark">
      <span class="brand-dot"></span>
      <span class="brand-name">Roving Gadget Mend Service</span>
    </div>
    <div class="divider"></div>
    <div class="contact-block">
      <h1 class="contact-name">Dorian P. Hale</h1>
      <p class="contact-title">Service Director</p>
      <p class="contact-address">P.O. Box 530697<br>Larkhaven, TX 77390</p>
      <p class="contact-lines">
        <span class="contact-label">T:</span>(281) 555-0148<br>
        <span class="contact-label">E:</span>dphale@corvanmail.com
      </p>
    </div>
    <div class="promo-band">
      <span>Expert Repair on All Major Brands &amp; Models.</span>
      <span>Mention this Special for $15 Off Any Job Requiring Parts!</span>
    </div>
  </div>
</body>
</html>
```